Business Card Design

- one on one personal training
- group personal training
- indoor or outdoor training available
- fitness and health assessments
- personalised fitness programs
- flexible hours for training

I am a Personal Trainer in Perth Australia. I am looking to expand my word of mouth client base.

I would like to see something that uses the colours blue, green and/or yellow.

The final design should reflect the way that I train clients, fun, motivating and perhaps a little quirky?
Updates

update with a logo with the letters MPT thank you

Hi all, Have had some great designs so far. Have decided to go double sided, perhaps to use the back to list my services. Thank you

Please check update brief. Thank you.

Target Market(s)

Professionals, ages 30 to 60

Industry/Entity Type

Training

Contact Information for Business Card

Mira Ostrowski
Personal Trainer

0491 570 118
mirapersonaltrainer@quillnest.com
http://www.mirapersonaltrainer.net

Requirements
Must have
• A logo with the letter MPT
Nice to have
• a logo to represent either; fitness, health, change, overall well-being.
Should not have
• Please no weights or lotus flowers!!

```html
<!DOCTYPE html>
<html lang="en">
<head>
<meta charset="utf-8">
<title>Mira Ostrowski – Personal Trainer Business Card</title>
<link rel="stylesheet" href="https://fonts.googleapis.com/css2?family=Open+Sans:wght@400;600&display=swap">
<style>
  :root {
    --page: #3b3b3b;
    --white: #ffffff;
    --card-black: #141414;
    --card-black-light: #262626;
    --bronze: #9a6a45;
    --bronze-light: #c89a72;
    --steel: #8a98a4;
    --ink: #f2f2f2;
    --divider: #3a3a3a;
  }
  * { margin: 0; padding: 0; box-sizing: border-box; }
  html, body {
    width: 1200px; height: 750px; overflow: hidden;
    background: var(--page);
    font-family: "Open Sans", Arial, sans-serif;
  }
  .canvas { position: relative; width: 1200px; height: 750px; }

  .card {
    position: absolute; top: 211px;
    width: 511px; height: 293px;
    border-radius: 20px; overflow: hidden;
  }
  .card--front { left: 78px; background: var(--white); }
  .card--back {
    left: 609px;
    background: radial-gradient(ellipse at 50% 45%, var(--card-black-light), var(--card-black) 75%);
  }

  /* front */
  .brand {
    position: absolute; left: 80px; top: 44px;
    display: flex; align-items: center; gap: 14px;
  }
  .brand__mark {
    width: 46px; height: 46px; border-radius: 50%;
    background: var(--bronze);
  }
  .brand__name {
    font-size: 26px; font-weight: 600; color: var(--bronze);
    line-height: 1.15;
  }
  .brand__role {
    font-size: 26px; font-weight: 600; color: var(--bronze);
    line-height: 1.15;
  }
  .stripe {
    position: absolute; left: 0; width: 100%;
  }
  .stripe--bronze { top: 147px; height: 6px; background: linear-gradient(var(--bronze-light), var(--bronze)); }
  .stripe--steel { top: 155px; height: 6px; background: linear-gradient(#c3ccd3, var(--steel)); }
  .front__lower {
    position: absolute; left: 0; top: 161px; width: 100%; height: 132px;
    background: linear-gradient(180deg, #0d0d0d, var(--card-black-light));
    color: var(--ink);
  }
  .holder { position: absolute; left: 30px; top: 28px; }
  .holder__name { font-size: 17px; line-height: 1.3; }
  .holder__role { font-size: 13.5px; line-height: 1.4; }
  .divider {
    position: absolute; left: 186px; top: 28px; width: 2px; height: 62px;
    background: var(--divider);
  }
  .contact { position: absolute; left: 222px; top: 28px; list-style: none; }
  .contact__item {
    display: flex; align-items: center; gap: 12px;
    font-size: 15px; line-height: 18px; height: 18px;
  }
  .contact__icon { width: 14px; height: 14px; fill: none; stroke: var(--ink); stroke-width: 1.3; }
  .contact__icon--solid { fill: var(--ink); stroke: none; }

  /* back */
  .back__mark {
    position: absolute; left: 34px; top: 88px;
    display: flex; align-items: center; gap: 10px;
  }
  .back__mark-dot { width: 40px; height: 40px; border-radius: 50%; background: var(--bronze); }
  .back__mark-name { font-size: 17px; font-weight: 600; color: var(--bronze-light); }
  .services {
    position: absolute; left: 221px; top: 135px; list-style: none;
    color: var(--ink); font-size: 15.5px; line-height: 17.4px;
  }
</style>
</head>
<body>
<main class="canvas">
  <section class="card card--front">
    <div class="brand">
      <span class="brand__mark"></span>
      <div>
        <div class="brand__name">Mira Ostrowski</div>
        <div class="brand__role">Personal Trainer</div>
      </div>
    </div>
    <div class="stripe stripe--bronze"></div>
    <div class="stripe stripe--steel"></div>
    <div class="front__lower">
      <div class="holder">
        <div class="holder__name">Mira Ostrowski</div>
        <div class="holder__role">Personal Trainer</div>
      </div>
      <div class="divider"></div>
      <ul class="contact">
        <li class="contact__item">
          <svg class="contact__icon contact__icon--solid" viewBox="0 0 14 14" aria-hidden="true"><path d="M1 4 Q7 0 13 4 L11 6 L9 5 L9 4 Q7 3 5 4 L5 5 L3 6 Z M3 7 H11 V12 H3 Z"/></svg>
          <span>0491 570 118</span>
        </li>
        <li class="contact__item">
          <svg class="contact__icon" viewBox="0 0 14 14" aria-hidden="true"><rect x="1" y="3" width="12" height="8" fill="#f2f2f2"/><path d="M1 3 L7 8 L13 3" stroke="#141414"/></svg>
          <span>mirapersonaltrainer@quillnest.com</span>
        </li>
        <li class="contact__item">
          <svg class="contact__icon" viewBox="0 0 14 14" aria-hidden="true"><circle cx="7" cy="7" r="5.5"/><ellipse cx="7" cy="7" rx="2.4" ry="5.5"/><path d="M1.5 7 H12.5 M2.5 4 H11.5 M2.5 10 H11.5"/></svg>
          <span>www.mirapersonaltrainer.net</span>
        </li>
      </ul>
    </div>
  </section>

  <section class="card card--back">
    <div class="back__mark">
      <span class="back__mark-dot"></span>
      <span class="back__mark-name">Mira Ostrowski</span>
    </div>
    <ul class="services">
      <li>one on one personal training</li>
      <li>group personal training</li>
      <li>indoor or outdoor training available</li>
      <li>fitness and health assessments</li>
      <li>personalised fitness programs</li>
      <li>flexible hours for training</li>
    </ul>
  </section>
</main>
</body>
</html>
```